Flyer for an pediatric sleep consultancy - to distribute to play and childcare centers etc.

I need a flyer that will attract the attention of parents with children between the age of babies to toddlers, who may be experiencing sleep issues. The flyer will be placed at places such as community centers, doctors room, play centers, kindergardens, etc.

My company is called "The Quiet Meadow Nest" and provides a sleep consultancy service. My service essentially provides a customized plan for parents to follow and general advice and guidance. It is not medical advice.

I like to the flyer to have an overall tone that is soft and peaceful with a clean and beautiful design, however can catch the attention of parents who may be struggling with their child's sleep issues and are sleep deprived. I would like photos with minimal text. The colour I use is a brownish rose. I will attach some of my designs to give you an idea. You can have a look at my homepage as well to get an idea about my esthetic direction and the colour. Although the colour of my page is a bit too brownish....

I will provide the text to appear in the flyer once I have a better idea of the layout that I prefer for the flyer. The text however wont be extensive, just some catchy points.

I want to direct people to my website which is www.thequietmeadownest.example
I offer a first FREE evaluation call, to the parents, to get to know each other better, learn about their child's particular sleep problems and see if we are a good fit and can work together. I would like to have this information somehow on the flyer, so that the parents will contact me.
I also have a facebook page, which is: The Quiet Meadow Nest

I have a logo that I would like to appear on the flyer. I will attach the file once the uploader on pixel fair is fixed.

When I print the flyer - I like to print A5 SIZE ... please make sure the formatting is OK for this size.

Here are some text ideas. of course all of it would be too much, I guess. On the front of the flyer I would like to have some catchy phrase or something similar to get people interested and to want to know more. On the back there could be a bit more text and information. But I'm open too suggestions....
I'm not too sure about the wording yet. But here are some text that I might be use:

Is sleep an issue in your home?

Is your baby having trouble sleeping? ... are you?!
I can help!

Sleep, baby, sleep….

Teaching children how to sleep

The Quiet Meadow Nest is a pediatric sleep consultancy that specializes in helping parents with children who struggle to develop good and healthy sleep habits.
Disruptive sleep patterns or not enough sleep can affect the physical, mental and emotional development of your child.

Of course nobody plans to have a sleep problem, but habits can become easily ingrained and spiral quickly out of control and you can find yourself sleep deprived, desperate and not too sure what to do. You see all the other sleeping babies and wish there was someone who understood what you were going through?! Well, there is!

Contact me for a free 15 minute consultation.

This 15 minute „mini“ consultation is a chance to discuss your unique sleep challenges and sleep goals with me. I will provide you with an overview of how I will work with your family to achieve your wildest sleep dreams (goals).
Furthermore do I understand and believe that every child and their family is unique and there is no one size fits all!
I would love to have a chat with you and talk about how I can help make things easier for you and your family!

Do I need a sleep consultant for my child?
The answer is yes if:
- if your child will only fall asleep when nursing or bottle feeding
- if your child needs a dummy or other external aid, like being rocked, patted or taken for a care ride to fall asleep
- if your good night routine is a challenging and exhausting procedure instead of a relaxed and enjoyable moment for the whole family
- if sleep is a constant battle in your home which leaves you feeling frustrated and exhausted
- if your own lack of sleep is taking a toll on you and the whole family

What can I do for you?

I will:

- Guide you to set an age appropriate foundation for good sleep
- Create an individual sleep plan tailored especially to your child’s sleep needs and circumstances
- Help you to teach your childto go to sleep and get back to sleep independently during the night
- show you how to teach your child to take healthful, restorative naps
-Learn

Contact:

Marta Lindqvist
info@thequietmeadownest.example
www.thequietmeadownest.example
+34 612 384 570

Consultations in English, German or Spanish via Phone/Video Call or home consultation

Reason: I have to go on a business trip and won't be able to choose a design until the deadline. During the trip I won't have time to give feedback and ask for changes. thank you

Target Market(s)

parents, sleep deprived mothers, young families, child care provider,

Industry/Entity Type

Baby Care

Contact Information for Business Card

Marta Lindqvist
pediatric sleep consultant
+34 612 384 570

```html
<!DOCTYPE html>
<html lang="en">
<head>
<meta charset="utf-8">
<title>The Quiet Meadow Nest – Flyer</title>
<link rel="stylesheet" href="https://fonts.googleapis.com/css2?family=Open+Sans:wght@300;400;600;700&family=Raleway:wght@300;400;600;700&family=Parisienne&family=Yanone+Kaffeesatz:wght@300;400&family=Cormorant+Garamond:ital@1&display=swap">
<style>
  :root {
    --stage: #3d3d3f;
    --paper: #ffffff;
    --rose: #c0857a;
    --rose-deep: #b27468;
    --rose-muted: #b9948b;
    --blush: #f7e4df;
    --blush-soft: #fbf0ee;
    --sage: #8f9b96;
    --sage-tab: #97a39d;
    --ink: #5c5456;
    --ink-soft: #8a8284;
    --white: #ffffff;
  }
  * { box-sizing: border-box; margin: 0; padding: 0; }
  html, body { width: 1200px; height: 870px; overflow: hidden; background: var(--stage); }
  .stage { position: relative; width: 1200px; height: 870px; }
  .page {
    position: absolute; top: 77px; width: 507px; height: 710px;
    background: var(--paper); overflow: hidden;
    box-shadow: 4px 6px 14px rgba(0,0,0,.45);
    font-family: "Open Sans", sans-serif;
  }
  .page--front { left: 71px; }
  .page--back { left: 610px; background: linear-gradient(160deg, #f8e6e6 0%, #fbeeee 45%, #f7e2dc 100%); }
  .abs { position: absolute; }

  /* ---------- front ---------- */
  .hero-photo {
    left: 0; top: 95px; width: 470px; height: 320px;
    background: radial-gradient(ellipse at 45% 55%, #f3dccd 0%, #efe6dd 35%, #f4f1ec 60%, #ffffff 85%);
  }
  .crib-photo {
    left: 0; top: 440px; width: 507px; height: 215px;
    background: linear-gradient(180deg, #ffffff 0%, #f3efec 40%, #eee4de 70%, #f6f1ee 100%);
  }
  .brand-mark { left: 25px; top: 28px; width: 300px; }
  .brand-mark__dot { position: absolute; left: 102px; top: 0; width: 42px; height: 42px; border: 1.5px solid var(--rose); border-radius: 50%; }
  .brand-mark__name { position: absolute; left: 0; top: 44px; font-family: "Raleway", sans-serif; font-weight: 300; font-size: 19px; color: #8a7f80; white-space: nowrap; }
  .social { left: 50px; top: 222px; width: 70px; text-align: center; }
  .social__square { width: 36px; height: 36px; background: var(--rose-muted); margin: 0 auto 4px 15px; }
  .social__name { font-family: "Raleway", sans-serif; font-size: 8px; color: var(--rose); letter-spacing: .3px; line-height: 10px; text-align: left; }
  .tagline { left: 185px; top: 127px; font-family: "Parisienne", cursive; font-size: 20px; color: var(--rose-muted); white-space: nowrap; }
  .title-script { left: 229px; top: 150px; font-family: "Parisienne", cursive; font-size: 36px; color: var(--rose); white-space: nowrap; }
  .swoosh { left: 0; top: 0; width: 507px; height: 710px; }
  .badge {
    left: 337px; top: 227px; width: 152px; height: 152px; border-radius: 50%;
    background: var(--rose-muted); border: 3px solid var(--white);
    box-shadow: 0 0 0 1.5px var(--rose-muted), 2px 3px 6px rgba(0,0,0,.25);
    display: flex; align-items: center; justify-content: center; text-align: center;
    color: var(--white); font-weight: 700; font-size: 17.5px; line-height: 21px;
    text-shadow: 1px 1px 2px rgba(0,0,0,.3);
  }
  .question { left: 29px; top: 405px; font-family: "Raleway", sans-serif; font-weight: 300; color: var(--rose); }
  .question__lead { font-size: 22px; line-height: 25px; }
  .question__punch { font-size: 29px; line-height: 38px; }
  .question__help { font-weight: 700; font-size: 31px; color: var(--sage); line-height: 42px; }
  .front-phone { left: 293px; top: 413px; font-family: "Raleway", sans-serif; font-weight: 700; font-size: 25px; color: var(--rose); white-space: nowrap; }
  .front-blurb { right: 27px; top: 450px; width: 230px; text-align: right; font-family: "Raleway", sans-serif; font-weight: 300; font-size: 10.5px; line-height: 15px; color: var(--ink-soft); }
  .offer { left: 26px; top: 581px; width: 300px; font-family: "Cormorant Garamond", serif; font-style: italic; font-size: 12px; line-height: 16.5px; color: var(--ink-soft); }
  .url-bar { left: 0; top: 646px; width: 300px; height: 27px; background: var(--rose); border-radius: 0 14px 14px 0; }
  .url-bar__text { position: absolute; left: 16px; top: 0; font-family: "Yanone Kaffeesatz", sans-serif; font-size: 20px; line-height: 27px; color: var(--white); white-space: nowrap; }
  .contact-tab { left: 258px; top: 639px; width: 249px; height: 38px; background: var(--sage-tab); border-radius: 19px 0 0 19px; color: var(--white); text-align: right; padding-right: 12px; }
  .contact-tab__name { font-family: "Cormorant Garamond", serif; font-style: italic; font-size: 12px; line-height: 20px; padding-top: 1px; }
  .contact-tab__name strong { font-family: "Yanone Kaffeesatz", sans-serif; font-style: normal; font-weight: 400; font-size: 18px; }
  .contact-tab__mail { font-size: 10.5px; line-height: 13px; }
  .languages { left: 26px; top: 688px; font-size: 11px; color: var(--ink-soft); letter-spacing: .2px; white-space: nowrap; }

  /* ---------- back ---------- */
  .top-photo {
    left: 18px; top: 27px; width: 281px; height: 138px; border-radius: 8px;
    border: 4px solid #dcc6b4;
    background: linear-gradient(120deg, #f4e6dc 0%, #eed6c8 45%, #f7efea 100%);
  }
  .back-url { left: 33px; top: 179px; font-family: "Yanone Kaffeesatz", sans-serif; font-size: 27px; color: var(--rose); white-space: nowrap; letter-spacing: .5px; }
  .toddler-photo {
    left: 0; top: 219px; width: 290px; height: 404px;
    background: linear-gradient(180deg, #dcd9d7 0%, #e8e2de 40%, #d7c6bd 80%, #e9d2c7 100%);
  }
  .intro { left: 306px; top: 33px; width: 180px; text-align: right; font-size: 9.8px; line-height: 12.5px; color: var(--ink); }
  .intro p + p { margin-top: 12px; }
  .invite { left: 306px; top: 286px; width: 180px; text-align: right; font-family: "Raleway", sans-serif; font-size: 12.5px; line-height: 15.5px; color: var(--ink); }
  .circle-photo { border-radius: 50%; border: 3px solid var(--white); box-shadow: 0 0 0 1px var(--rose-muted); }
  .circle-photo--small { left: 189px; top: 221px; width: 100px; height: 100px; background: radial-gradient(circle at 40% 45%, #f2dcd0, #f6eeea 70%); }
  .circle-photo--large { left: 305px; top: 397px; width: 180px; height: 180px; background: radial-gradient(circle at 50% 40%, #e9cdbd, #f5f2f1 70%); }
  .back-headline { left: 30px; top: 477px; width: 260px; color: var(--white); font-weight: 600; font-size: 21.5px; line-height: 30px; text-shadow: 1px 1px 3px rgba(0,0,0,.45); letter-spacing: -.3px; }
  .back-headline p + p { margin-top: 6px; }
  .phone-bar { left: 0; top: 623px; width: 234px; height: 33px; background: var(--rose-muted); border-radius: 0 16px 16px 0; }
  .phone-bar__text { position: absolute; left: 22px; top: 0; font-family: "Raleway", sans-serif; font-size: 22px; line-height: 33px; color: var(--white); letter-spacing: 1px; white-space: nowrap; }
  .mail-bar { left: 0; top: 664px; width: 226px; height: 22px; background: var(--rose-muted); border-radius: 0 11px 11px 0; }
  .mail-bar__text { position: absolute; left: 24px; top: 0; font-family: "Cormorant Garamond", serif; font-style: italic; font-size: 9.5px; line-height: 22px; color: var(--white); white-space: nowrap; }
  .back-languages { left: 330px; top: 612px; width: 150px; text-align: center; font-weight: 700; font-size: 12px; line-height: 15.5px; color: #3f3a3b; }
</style>
</head>
<body>
<main class="stage">

  <!-- front -->
  <section class="page page--front">
    <div class="abs hero-photo" role="img" aria-label="Photo of a smiling baby in a soft knitted hat"></div>
    <div class="abs crib-photo" role="img" aria-label="Photo of a newborn sleeping in a white crib"></div>

    <svg class="abs swoosh" viewBox="0 0 507 710" aria-hidden="true">
      <path d="M0 300 C 120 320, 200 395, 300 380 C 390 365, 440 230, 507 120 L 507 150 C 450 250, 400 395, 300 410 C 190 425, 110 360, 0 350 Z" fill="#c49589"/>
      <path d="M0 350 C 110 360, 190 425, 300 410 C 400 395, 450 250, 507 150 L 507 170 C 460 270, 410 418, 300 432 C 190 446, 100 390, 0 372 Z" fill="#ffffff" opacity=".85"/>
    </svg>

    <div class="abs brand-mark">
      <span class="brand-mark__dot"></span>
      <span class="brand-mark__name">The Quiet Meadow Nest</span>
    </div>

    <div class="abs tagline">Is sleep an issue in your home?</div>
    <div class="abs title-script">Sleep Baby Sleep</div>

    <div class="abs social">
      <div class="social__square"></div>
      <div class="social__name">THE QUIET<br>MEADOW NEST</div>
    </div>

    <div class="abs badge">Contact me<br>for a FREE<br>15 Minute<br>Consultation</div>

    <div class="abs question">
      <div class="question__lead">Is your baby having<br>trouble sleeping?...</div>
      <div class="question__punch">Are you?!</div>
      <div class="question__help">I can help!</div>
    </div>

    <div class="abs front-phone">+34 612 384 570</div>
    <p class="abs front-blurb">This 15 minute „mini“ consultation is a chance to discuss your unique sleep challenges and sleep goals with me.</p>

    <p class="abs offer">I offer a first FREE evaluation call, to the parents, to get to know each other better, learn about their child's particular sleep problems and see if we are a good fit and can work together.</p>

    <div class="abs url-bar"><span class="url-bar__text">www.thequietmeadownest.example</span></div>
    <div class="abs contact-tab">
      <div class="contact-tab__name">Contact me: <strong>Marta Lindqvist</strong></div>
      <div class="contact-tab__mail">info@thequietmeadownest.example</div>
    </div>

    <p class="abs languages">Consultations in English, German or Spanish via Phone/Video Call or home consultation</p>
  </section>

  <!-- back -->
  <section class="page page--back">
    <div class="abs toddler-photo" role="img" aria-label="Photo of a toddler in pyjamas standing at a crib"></div>

    <svg class="abs swoosh" viewBox="0 0 507 710" aria-hidden="true">
      <path d="M0 219 L 290 219 L 290 623 L 0 623 Z" fill="none"/>
      <path d="M250 300 C 330 380, 420 470, 440 560 C 455 630, 460 680, 460 710 L 507 710 L 507 620 C 490 520, 400 400, 285 300 Z" fill="#f2cdbf" opacity=".8"/>
      <path d="M250 305 C 340 390, 410 480, 420 570 C 428 630, 430 680, 430 710 L 470 710 C 470 650, 462 580, 445 520 C 420 430, 350 360, 278 300 Z" fill="#c49589"/>
    </svg>

    <div class="abs top-photo" role="img" aria-label="Photo of a mother resting beside her sleeping baby"></div>
    <div class="abs back-url">thequietmeadownest.example</div>

    <div class="abs intro">
      <p>The Quiet Meadow Nest is a pediatric sleep consultancy that specializes in helping parents with children who struggle to develop good and healthy sleep habits.</p>
      <p>Disruptive sleep patterns or not enough sleep can affect the physical, mental and emotional development of your child.</p>
      <p>Of course nobody plans to have a sleep problem, but habits can become easily ingrained and spiral quickly out of control and you can find yourself sleep deprived, desperate and not too sure what to do. You see all the other sleeping babies and wish there was someone who understood what you were going through?! Well, there is!</p>
    </div>

    <p class="abs invite">I would love to have a chat with you and talk about how I can help make things easier for you and your family!</p>

    <div class="abs circle-photo circle-photo--small" role="img" aria-label="Photo of a baby sleeping on a white pillow"></div>
    <div class="abs circle-photo circle-photo--large" role="img" aria-label="Photo of a baby peeking over a white blanket"></div>

    <div class="abs back-headline">
      <p>Do I need a sleep consultant for my child?</p>
      <p>If answer is YES,<br>Please call me</p>
    </div>

    <div class="abs phone-bar"><span class="phone-bar__text">+34 612 384 570</span></div>
    <div class="abs mail-bar"><span class="mail-bar__text">Marta Lindqvist: info@thequietmeadownest.example</span></div>

    <p class="abs back-languages">Consultations in English, German or Spanish via Phone/Video Call or home consultation</p>
  </section>

</main>
</body>
</html>
```